Hydroponic Farm Needs a Business Card

We need a business card design for a hydroponic farm located on the Gulf Coast called 'Mossbrook Farms'. We grow many forms of lettuce and tomatoes along with other herbs and spices. We currently sell to farmer's markets though will soon be expanding to commercial accounts such as restaurants and grocery stores. The colors should be bright and vibrant to reflect the nature of our produce. The final design should communicate a professional, clean, yet friendly impression and able to be used both with farmer's markets and commercial accounts.

The pictures are an example of our product. The pictures do not have to be incorporated into the business card design.

Please put areas for information such as Names, Phone Number, E-mail address, and additional information.

Farm

```html
<!DOCTYPE html>
<html lang="en">
<head>
<meta charset="UTF-8">
<title>Mossbrook Farms – Business Card</title>
<link rel="stylesheet" href="https://fonts.googleapis.com/css2?family=Bebas+Neue&display=swap">
<style>
  :root {
    --backdrop: #ece9e2;
    --paper: #ffffff;
    --leaf: #5cb946;
    --forest: #1f6a39;
    --forest-deep: #0f4322;
    --coral: #e0474c;
    --shadow: rgba(40, 30, 20, 0.28);
  }
  * { box-sizing: border-box; margin: 0; padding: 0; }
  html, body {
    width: 1200px;
    height: 900px;
    overflow: hidden;
    background: var(--backdrop);
    font-family: "Bebas Neue", "Arial Narrow", sans-serif;
  }
  .card {
    position: absolute;
    width: 560px;
    height: 320px;
    background: var(--paper);
    overflow: hidden;
    box-shadow: 0 10px 28px var(--shadow);
  }

  /* Front */
  .card--front { left: 90px; top: 90px; }
  .front__band {
    position: absolute;
    inset: 0;
    background: linear-gradient(160deg, var(--forest) 0%, var(--forest-deep) 100%);
    clip-path: polygon(0 72%, 100% 38%, 100% 100%, 0 100%);
  }
  .front__brand {
    position: absolute;
    left: 0; right: 0;
    top: 30px;
    display: flex;
    flex-direction: column;
    align-items: center;
    transform: rotate(-11deg);
    transform-origin: 280px 120px;
  }
  .brand__dot {
    width: 74px;
    height: 74px;
    border-radius: 50%;
    background: var(--leaf);
    margin-bottom: 8px;
  }
  .brand__name {
    color: var(--leaf);
    font-size: 50px;
    line-height: 1;
    letter-spacing: 1px;
  }

  /* Back */
  .card--back { left: 550px; top: 490px; }
  .back__band {
    position: absolute;
    inset: 0;
    background: linear-gradient(160deg, var(--forest) 0%, var(--forest-deep) 100%);
    clip-path: polygon(0 92%, 100% 62%, 100% 100%, 0 100%);
  }
  .back__tagline {
    position: absolute;
    left: 130px;
    top: 262px;
    width: 420px;
    text-align: center;
    color: var(--paper);
    font-size: 20px;
    line-height: 1;
    letter-spacing: 0.5px;
    white-space: nowrap;
    transform: rotate(-9.7deg);
  }
  .back__bar {
    position: absolute;
    left: 200px;
    top: 0;
    width: 24px;
    height: 122px;
    background: var(--forest);
  }
  .back__rule {
    position: absolute;
    left: 292px;
    top: 60px;
    width: 3px;
    height: 180px;
    background: var(--forest);
  }
  .person {
    position: absolute;
    right: 336px;
    top: 160px;
    text-align: right;
    color: var(--leaf);
    line-height: 1;
  }
  .person__name { font-size: 32px; }
  .person__role { font-size: 18px; margin-top: 2px; }

  .contacts {
    position: absolute;
    left: 280px;
    top: 40px;
    list-style: none;
  }
  .contact {
    display: flex;
    align-items: center;
    height: 30px;
    margin-bottom: 4px;
  }
  .contact__icon {
    width: 28px;
    height: 28px;
    background: var(--coral);
    display: flex;
    align-items: center;
    justify-content: center;
    border-radius: 3px;
    position: relative;
    z-index: 1;
  }
  .contact__text {
    margin-left: 14px;
    color: var(--leaf);
    font-size: 20px;
    letter-spacing: 0.5px;
  }
</style>
</head>
<body>

<section class="card card--front" aria-label="Business card front">
  <div class="front__band"></div>
  <div class="front__brand">
    <div class="brand__dot"></div>
    <div class="brand__name">MOSSBROOK FARMS</div>
  </div>
</section>

<section class="card card--back" aria-label="Business card back">
  <div class="back__band"></div>
  <div class="back__bar"></div>
  <div class="back__rule"></div>

  <div class="person">
    <div class="person__name">EMPLOYEE NAME</div>
    <div class="person__role">DESIGNATION</div>
  </div>

  <ul class="contacts">
    <li class="contact">
      <span class="contact__icon">
        <svg width="16" height="16" viewBox="0 0 24 24" aria-hidden="true">
          <path fill="#fff" d="M6.6 10.8a15.1 15.1 0 0 0 6.6 6.6l2.2-2.2a1 1 0 0 1 1-.25 11.4 11.4 0 0 0 3.6.57 1 1 0 0 1 1 1V20a1 1 0 0 1-1 1A17 17 0 0 1 3 4a1 1 0 0 1 1-1h3.5a1 1 0 0 1 1 1c0 1.25.2 2.45.57 3.57a1 1 0 0 1-.25 1z"/>
        </svg>
      </span>
      <span class="contact__text">123-456-789</span>
    </li>
    <li class="contact">
      <span class="contact__icon">
        <svg width="16" height="16" viewBox="0 0 24 24" aria-hidden="true">
          <circle cx="12" cy="12" r="4" fill="none" stroke="#fff" stroke-width="2.2"/>
          <path d="M16 8v5.5a2.5 2.5 0 0 0 5 0V12a9 9 0 1 0-3.5 7.1" fill="none" stroke="#fff" stroke-width="2.2" stroke-linecap="round"/>
        </svg>
      </span>
      <span class="contact__text">EMAIL@DOMAIN.COM</span>
    </li>
    <li class="contact">
      <span class="contact__icon">
        <svg width="16" height="16" viewBox="0 0 24 24" aria-hidden="true">
          <g fill="none" stroke="#fff" stroke-width="1.8">
            <circle cx="12" cy="12" r="9"/>
            <ellipse cx="12" cy="12" rx="4" ry="9"/>
            <path d="M3 12h18M5 7h14M5 17h14"/>
          </g>
        </svg>
      </span>
      <span class="contact__text">WWW.WEBSITE.COM</span>
    </li>
    <li class="contact">
      <span class="contact__icon">
        <svg width="16" height="16" viewBox="0 0 24 24" aria-hidden="true">
          <path fill="#fff" d="M3 10l9-6 9 6v2H3z"/>
          <path fill="#fff" d="M5 13h2v6H5zM9 13h2v6H9zM13 13h2v6h-2zM17 13h2v6h-2zM3 20h18v2H3z"/>
        </svg>
      </span>
      <span class="contact__text">STORE ADDRESS</span>
    </li>
  </ul>

  <div class="back__tagline">SPECIALITIES OF THE INDUSTRY, MAIN ATTRACTIONS ETC.</div>
</section>

</body>
</html>
```